Ledger Grove Pilot Banner Ad campaign

We are the number 1 leading automated journal & analytics platform for active traders in the crypto space

We will be running banner ads on a specialist ad network and need HTML designs + a good strategy.

Some of our key selling points to consider including:

- The #1 automated journaling & analytics solution for Crypto Traders
- We save traders time (from manual data entry that can be automated by our journal trade import service)
- We help traders improve through detailed analytics feedback on their trading performance
- LGP has helped thousands of crypto traders improve performance
- 5,700+ traders are using LGP to save themselves hundreds of data entry hours per year
- Analyse your full trade history in a click!

I have attached an example mockup we came up with internally but we are not professionals. Use it as a guide to heavily improve upon in the context of general design quality, and 'sales-y' lingo to improve conversions
Updates

Have added a £100 1st place payment increase upon advice from a designer Should incentivise the best of the best to submit work

Target Market(s)

Active traders in the crypto derivatives space. Trading on the following exchanges:

- Trelvax.example
- Quorvane.example
- Pelmiro.example
- ZQB.example

Font styles to use
Other font styles liked:
• Quicksand is our main font atm

Colors
3277b5
33a6d7
0792cd
85abd2
3276b5
85acd3
85cae6
86cae7

Requirements
Must have
• similar colour scheme from my example upload.

Check our main website for more: ledgergrovepilot.example

Although bare in mind, its a bit old and shitty. We are now working with specialists to improve, so feel free to have some creative freedom
Nice to have
• Nice clear custom icons to accompany text. And a rotation of 2 or 3 of the main selling points from the project description

```html
<!DOCTYPE html>
<html lang="en">
<head>
<meta charset="utf-8">
<title>Ledger Grove Pilot – Banner Set</title>
<link href="https://fonts.googleapis.com/css2?family=Quicksand:wght@400;500;600;700&display=swap" rel="stylesheet">
<style>
  :root {
    --page-bg: #eeeeee;
    --banner-top: #03a8cb;
    --banner-mid: #0e8fca;
    --banner-bottom: #2470b9;
    --accent: #f9f01a;
    --text-light: #ffffff;
    --icon-tone-a: #86cae7;
    --icon-tone-b: #85abd2;
    --cta-text: #111111;
  }
  * { box-sizing: border-box; margin: 0; padding: 0; }
  html, body {
    width: 1013px; height: 1200px; overflow: hidden;
    background: var(--page-bg);
    font-family: "Quicksand", sans-serif;
  }
  .sheet { position: relative; width: 1013px; height: 1200px; }
  .banner {
    position: absolute; width: 382px; height: 320px;
    background: linear-gradient(180deg, var(--banner-top) 0%, var(--banner-mid) 55%, var(--banner-bottom) 100%);
    color: var(--text-light); overflow: hidden;
  }
  .col-left { left: 102px; }
  .col-right { left: 528px; }
  .row-1 { top: 44px; }
  .row-2 { top: 432px; }
  .row-3 { top: 836px; }

  .brand {
    position: absolute; left: 54px; top: 28px;
    display: flex; align-items: center; gap: 12px;
  }
  .brand-mark {
    width: 24px; height: 24px; border: 1.5px solid var(--text-light);
  }
  .brand-name {
    font-size: 18px; font-weight: 400; letter-spacing: 0.5px;
    text-transform: uppercase; white-space: nowrap;
  }

  .feature-art {
    position: absolute; border-radius: 8px;
    background: linear-gradient(160deg, var(--icon-tone-a), var(--icon-tone-b));
    opacity: 0.75;
  }

  .message { position: absolute; line-height: 1.3; font-weight: 500; }
  .hl { color: var(--accent); }

  .cta {
    position: absolute; left: 75px; top: 230px;
    width: 231px; height: 42px; border-radius: 21px;
    background: var(--accent); color: var(--cta-text);
    font-size: 12.5px; font-weight: 600; letter-spacing: 0.3px;
    display: flex; align-items: center; justify-content: center;
    box-shadow: 2px 3px 6px rgba(0, 0, 0, 0.25);
  }

  /* banner 1 */
  .b1 .message { left: 174px; top: 84px; font-size: 15.5px; }
  .b1 .rank-lead { font-size: 16px; }
  .b1 .rank { font-size: 28px; font-weight: 700; margin-left: 8px; }
  /* banner 2 */
  .b2 .message { left: 183px; top: 108px; font-size: 26px; line-height: 1.1; }
  .b2 .big { font-size: 29px; display: block; }
  .b2 .note { display: block; font-size: 7px; text-align: center; margin-top: 6px; line-height: 1.4; width: 176px; }
  /* banner 3 */
  .b3 .message { left: 177px; top: 86px; font-size: 14.5px; line-height: 1.38; }
  /* banner 4 */
  .b4 .message { left: 175px; top: 89px; font-size: 15px; line-height: 1.3; }
  .b4 .stat { font-size: 17.5px; }
  /* banner 5 */
  .b5 .message { left: 180px; top: 102px; font-size: 13.8px; line-height: 1.3; }
  /* banner 6 */
  .b6 .message { left: 188px; top: 94px; font-size: 15.5px; line-height: 1.45; }
  .b6 .lead { font-size: 22px; display: block; line-height: 1.2; }
</style>
</head>
<body>
<main class="sheet">

  <section class="banner col-left row-1 b1">
    <div class="brand"><span class="brand-mark"></span><span class="brand-name">Ledger Grove Pilot</span></div>
    <div class="feature-art" role="img" aria-label="Outline icon of a monitor showing coin, chart, landscape and list panels" style="left:47px;top:84px;width:116px;height:106px;"></div>
    <p class="message"><span class="rank-lead">The</span><span class="rank hl">#1</span><br>Automated Journaling &amp;<br>Analytics Solution for<br>Crypto Traders</p>
    <a class="cta">START YOUR FREE TRIAL NOW</a>
  </section>

  <section class="banner col-right row-1 b2">
    <div class="brand"><span class="brand-mark"></span><span class="brand-name">Ledger Grove Pilot</span></div>
    <div class="feature-art" role="img" aria-label="Outline icon of a report with rising chart and a stopwatch in a hand" style="left:46px;top:82px;width:110px;height:110px;"></div>
    <p class="message">We <span class="hl">save</span><span class="big">traders time</span><span class="note">(from manual data entry that can be automated<br>by our journal trade import service)</span></p>
    <a class="cta">START YOUR FREE TRIAL NOW</a>
  </section>

  <section class="banner col-left row-2 b3">
    <div class="brand"><span class="brand-mark"></span><span class="brand-name">Ledger Grove Pilot</span></div>
    <div class="feature-art" role="img" aria-label="Outline icon of rising arrows above gears with a thumbs up" style="left:36px;top:71px;width:108px;height:107px;"></div>
    <p class="message">We help <span class="hl">traders improve</span><br>through detailed analytics<br>feedback on their trading<br>performance</p>
    <a class="cta">START YOUR FREE TRIAL NOW</a>
  </section>

  <section class="banner col-right row-2 b4">
    <div class="brand"><span class="brand-mark"></span><span class="brand-name">Ledger Grove Pilot</span></div>
    <div class="feature-art" role="img" aria-label="Outline icon of a document, money bags and a keyboard" style="left:37px;top:79px;width:110px;height:99px;"></div>
    <p class="message"><span class="stat hl">5,700+ traders</span><br>are using&nbsp; LGP to save<br>themselves hundreds of<br>data entry hours per year</p>
    <a class="cta">START YOUR FREE TRIAL NOW</a>
  </section>

  <section class="banner col-left row-3 b5">
    <div class="brand"><span class="brand-mark"></span><span class="brand-name">Ledger Grove Pilot</span></div>
    <div class="feature-art" role="img" aria-label="Outline icon of a report, large gear and rising bar chart with arrow" style="left:53px;top:80px;width:104px;height:104px;"></div>
    <p class="message"><span class="hl">LGP</span> has helped thousands<br>of crypto traders improve<br>performance</p>
    <a class="cta">START YOUR FREE TRIAL NOW</a>
  </section>

  <section class="banner col-right row-3 b6">
    <div class="brand"><span class="brand-mark"></span><span class="brand-name">Ledger Grove Pilot</span></div>
    <div class="feature-art" role="img" aria-label="Outline icon of a browser window with dollar sign and pie chart above a shopping cart" style="left:60px;top:79px;width:100px;height:102px;"></div>
    <p class="message"><span class="lead hl">Analyse</span>your full trade history<br>in a click!</p>
    <a class="cta">START YOUR FREE TRIAL NOW</a>
  </section>

</main>
</body>
</html>
```